Cleaning and Maintenance Business card design

i provide a service which includes;
Professional Window Cleaning
Lawn Mowing
Gardening
Painting
Rubbish Removal
Commercial Cleaning
Property & Ground Maintenance
Pensioner discounts apply
Call now for an inquiry and free quote
`Double sided` (willing to pay any extra)
i would like a design that is not too crowded and straight to the point.
i want the reader to know exactly what the business is about from one glance.
i would like the logo to communicate the businesses 3 main aspects (window cleaning, lawn mowing, and Cleaning)
Thanks.
Contact Information for Business Card
Business name : Brick 4 Leaf*
* with subline 'Plus All The Odd Jobs' (smaller font)
Name: Tom Varkonisky
Mobile: 0417 582 903
Email: t.varkonisky@mailbrook.net
ABN: 47 915 230 861
`Double Sided`
Logo Text
Brick 4 Leaf

```html
<!DOCTYPE html>
<html lang="en">
<head>
<meta charset="utf-8">
<title>Brick 4 Leaf – Business Card</title>
<link href="https://fonts.googleapis.com/css2?family=Questrial&display=swap" rel="stylesheet">
<style>
  :root {
    --bg: #d9d9d7;
    --brown: #3b170c;
    --green-light: #e2f0a8;
    --green-mid: #b8d860;
    --green-deep: #93c02c;
    --title-green: #b3d94e;
    --band-fill: #c3df69;
    --badge-gold: #e8c661;
    --service-text: #a88a80;
    --cream: #f4ecc9;
  }
  * { box-sizing: border-box; margin: 0; padding: 0; }
  html, body {
    width: 1200px; height: 1200px; overflow: hidden;
    background: var(--bg);
    font-family: "Questrial", sans-serif;
    color: var(--brown);
  }
  .card {
    position: absolute;
    left: 190px;
    width: 820px; height: 500px;
    overflow: hidden;
    background: radial-gradient(ellipse at 45% 40%, var(--green-light) 0%, var(--green-mid) 55%, var(--green-deep) 100%);
    box-shadow: 0 10px 28px rgba(0,0,0,0.18);
  }
  .card--back { top: 60px; }
  .card--front { top: 640px; }

  /* Back side */
  .back-mark {
    position: absolute; left: 0; right: 0; top: 150px;
    display: flex; align-items: center; justify-content: center; gap: 26px;
  }
  .mark-dot {
    width: 130px; height: 130px; border-radius: 50%;
    background: var(--badge-gold);
  }
  .mark-name { font-size: 44px; color: var(--brown); }
  .back-strip {
    position: absolute; left: 0; right: 0; bottom: 0; height: 42px;
    background: var(--brown);
  }

  /* Front side */
  .front-header {
    position: absolute; left: 0; right: 0; top: 0; height: 112px;
    background: var(--brown);
  }
  .front-mark {
    position: absolute; left: 28px; top: 20px;
    display: flex; align-items: center; gap: 12px;
  }
  .front-mark .mark-dot { width: 72px; height: 72px; }
  .front-mark .mark-name { font-size: 18px; color: var(--cream); }
  .business-name {
    position: absolute; right: 34px; top: 30px;
    font-family: "Questrial", sans-serif;
    font-weight: 400;
    font-size: 50px; line-height: 1;
    color: var(--title-green);
  }
  .tagline {
    position: absolute; right: 34px; top: 122px;
    background: var(--band-fill);
    padding: 4px 14px;
    font-size: 21px;
    color: var(--brown);
  }
  .contact {
    position: absolute; right: 34px; top: 174px;
    list-style: none; text-align: right;
    font-size: 24px; line-height: 36px;
  }
  .contact__value { font-weight: 700; letter-spacing: 0.5px; }
  .front-footer {
    position: absolute; left: 0; right: 0; bottom: 0; height: 142px;
    background: var(--brown);
    display: flex; flex-direction: column; justify-content: center; align-items: center;
    color: var(--service-text);
    font-size: 19px; line-height: 28px; text-align: center;
  }
</style>
</head>
<body>
  <section class="card card--back" aria-label="Card back">
    <div class="back-mark">
      <span class="mark-dot"></span>
      <span class="mark-name">Brick 4 Leaf</span>
    </div>
    <div class="back-strip"></div>
  </section>

  <section class="card card--front" aria-label="Card front">
    <header class="front-header">
      <div class="front-mark">
        <span class="mark-dot"></span>
        <span class="mark-name">Brick 4 Leaf</span>
      </div>
      <h1 class="business-name">Brick 4 Leaf</h1>
    </header>
    <p class="tagline">Plus All The Odd Jobs</p>
    <ul class="contact">
      <li>Name| <span class="contact__value">Tom Varkonisky</span></li>
      <li>Mobile| <span class="contact__value">0417 582 903</span></li>
      <li>Email| <span class="contact__value">t.varkonisky@mailbrook.net</span></li>
      <li>ABN| <span class="contact__value">47 915 230 861</span></li>
    </ul>
    <footer class="front-footer">
      <p>|Professional Window Cleaning|Lawn Mowing|Gardening|</p>
      <p>|Painting|Rubbish Removal|Commercial Cleaning|</p>
      <p>|Property &amp; Ground Maintenance|</p>
    </footer>
  </section>
</body>
</html>
```